Design professional, clean and neat beauty clinic

design an instagram style flyer similar style but have my own branding. Like they have their own. Must look different but also similar/better in professionalism. source file also needed.

Font styles to use
Sans Serif

```html
<!DOCTYPE html>
<html lang="en">
<head>
<meta charset="utf-8">
<title>Lumen Academy – Upcoming Courses</title>
<link rel="stylesheet" href="https://fonts.googleapis.com/css2?family=Anton&family=Montserrat:wght@400;500;600;700;800&display=swap">
<style>
:root{
  --page-bg:#e4e4e4;
  --paper:#ffffff;
  --ink:#333333;
  --ink-soft:#555555;
  --charcoal:#3a3a3a;
  --band-grey:#7a7a7a;
  --yellow:#f2d000;
  --yellow-soft:#f6e88a;
  --tint:#f4f4f4;
}
*{margin:0;padding:0;box-sizing:border-box}
html,body{width:1200px;height:2357px;overflow:hidden;background:var(--page-bg)}
body{position:relative;font-family:"Montserrat",sans-serif;color:var(--ink)}
.flyer{position:absolute;left:120px;top:578px;width:960px;height:1200px;background:var(--paper);overflow:hidden;box-shadow:0 6px 18px rgba(0,0,0,.18)}
.flyer-shapes{position:absolute;inset:0}
.brand{position:absolute;left:50px;top:66px;width:432px}
.brand-name{font-weight:600;font-size:45px;letter-spacing:1px;color:var(--ink);line-height:1;white-space:nowrap}
.brand-tagline{margin-top:14px;font-size:19px;font-weight:600;letter-spacing:1.5px;color:var(--ink);white-space:nowrap}
.cities{position:absolute;left:44px;top:183px;width:435px;height:36px;background:var(--band-grey);color:#fff;font-size:22px;font-weight:500;letter-spacing:.5px;display:flex;align-items:center;justify-content:center}
.headline{position:absolute;left:50px;top:265px;font-family:"Anton",sans-serif;font-weight:400;font-size:86px;line-height:86px;transform:scaleX(1.13);transform-origin:left top}
.headline .line-dark{color:var(--ink);display:block}
.headline .line-yellow{color:var(--yellow);display:block}
.offer-bar{position:absolute;left:42px;top:451px;width:440px;height:50px;background:var(--charcoal);color:#fff;font-weight:800;font-size:40px;letter-spacing:1px;padding-left:13px;display:flex;align-items:center;border-radius:4px 0 0 4px}
.courses{position:absolute;left:54px;top:561px;list-style:none}
.course{position:relative;height:124px;padding-left:104px;padding-top:8px}
.course-icon{position:absolute;left:0;top:0;width:82px;height:82px;border-radius:50%;background:var(--yellow)}
.course-date{font-size:26px;font-weight:400;color:var(--ink-soft);line-height:1.22}
.course-name{font-size:26px;font-weight:700;color:var(--ink);line-height:1.22}
.course-place{color:var(--yellow);font-weight:700}
.price{position:absolute;left:588px;top:856px;width:247px;text-align:center}
.price-only{height:48px;line-height:50px;color:#fff;font-weight:800;font-size:36px}
.price-amount{margin-top:8px;font-weight:800;font-size:74px;line-height:1;color:var(--ink)}
.price-note{margin-top:6px;font-weight:700;font-size:17px;line-height:1.08;color:var(--ink)}
.footer{position:absolute;left:0;bottom:0;width:960px;height:83px;background:var(--charcoal);color:#fff;font-weight:700;font-size:23px;letter-spacing:.5px;display:flex;align-items:center;justify-content:center;gap:20px}
</style>
</head>
<body>
<main class="flyer">
  <svg class="flyer-shapes" width="960" height="1200" viewBox="0 0 960 1200">
    <defs>
      <radialGradient id="portrait-tone" cx="40%" cy="45%" r="65%">
        <stop offset="0" stop-color="#e9c9b2"/>
        <stop offset=".55" stop-color="#c99c80"/>
        <stop offset="1" stop-color="#5a4236"/>
      </radialGradient>
      <linearGradient id="lower-tint" x1="0" y1="0" x2="0" y2="1">
        <stop offset="0" stop-color="#ffffff"/>
        <stop offset="1" stop-color="var(--tint)"/>
      </linearGradient>
    </defs>
    <rect x="0" y="540" width="960" height="580" fill="url(#lower-tint)"/>
    <circle cx="920" cy="640" r="360" fill="var(--yellow-soft)"/>
    <circle cx="950" cy="338" r="488" fill="var(--yellow)"/>
    <circle cx="950" cy="338" r="466" fill="url(#portrait-tone)" role="img" aria-label="Photo of a woman receiving a cosmetic injection near the eye"/>
    <polygon points="712,850 828,966 712,1082 596,966" fill="var(--yellow)" stroke="var(--yellow)" stroke-width="34" stroke-linejoin="round"/>
    <polygon points="576,880 588,856 588,904" fill="#222"/>
    <polygon points="847,880 835,856 835,904" fill="#222"/>
    <rect x="588" y="856" width="247" height="48" fill="var(--charcoal)"/>
  </svg>

  <header class="brand">
    <div class="brand-name">LUMEN ACADEMY</div>
    <div class="brand-tagline">INJECTABLES • SKIN • EDUCATION</div>
  </header>
  <div class="cities">MANCHESTER•BIRMINGHAM•LEEDS</div>

  <h1 class="headline"><span class="line-dark">UPCOMING</span><span class="line-yellow">COURSES</span></h1>
  <div class="offer-bar">SPECIAL OFFER</div>

  <ul class="courses">
    <li class="course"><span class="course-icon" role="img" aria-label="Toxin icon"></span>
      <div class="course-date">Tuesday 22nd January</div>
      <div class="course-name">Toxin <span class="course-place">(Manchester)</span></div></li>
    <li class="course"><span class="course-icon" role="img" aria-label="Lips icon"></span>
      <div class="course-date">Tuesday 29th January</div>
      <div class="course-name">Dermal Filler <span class="course-place">(Leeds)</span></div></li>
    <li class="course"><span class="course-icon" role="img" aria-label="Cheek icon"></span>
      <div class="course-date">Tuesday 5th February</div>
      <div class="course-name">Cheek Augmentation<br><span class="course-place">(Manchester)</span></div></li>
    <li class="course"><span class="course-icon" role="img" aria-label="Jawline icon"></span>
      <div class="course-date">Tuesday 12th February</div>
      <div class="course-name">Jawline/Chin Reshape<br><span class="course-place">(Leeds)</span></div></li>
  </ul>

  <div class="price">
    <div class="price-only">ONLY</div>
    <div class="price-amount">£499</div>
    <div class="price-note">PLUS VAT<br>IF BOOKED<br>BEFORE 2020</div>
  </div>

  <footer class="footer"><span>FINANCE OPTIONS AVAILABLE</span><span>|</span><span>BOOK YOUR PLACE TODAY</span></footer>
</main>
</body>
</html>
```